Body corporate management needs business principle flyer design

We need a one page A4 flyer design for our business principles.
We manage body corporates and strata properties.
Brightwick is a new initiative for our company. Its a label that we have given to our principles of business that drive our people, systems and processes to give assurance to our clients that every detail matters.
We would like to be able to include this design in future brochure so we are after 1 x portrait and 1 x landscape.
The design needs to portray professionalism.
We would like to see designs that use the colour red. (see attached logo).

Target Market(s)

Professionals

Industry/Entity Type

Business

Font styles to use
Sans Serif

Requirements
Must have
• Brightwick logo, provide the design file and as pdf
Nice to have
• the use of the colour red from the logo

```html
<!DOCTYPE html>
<html lang="en">
<head>
<meta charset="utf-8">
<title>Brightwick – Principles of Business</title>
<link rel="stylesheet" href="https://fonts.googleapis.com/css2?family=Arimo:wght@400;700&family=Open+Sans:wght@300;400;600&display=swap">
<style>
  :root {
    --red: #e8402f;
    --red-soft: #f2a48c;
    --ink: #1d1d1d;
    --body: #2a2a2a;
    --paper: #ffffff;
    --backdrop: #e9e7ec;
  }
  * { box-sizing: border-box; margin: 0; padding: 0; }
  html, body { width: 1200px; height: 1163px; overflow: hidden; background: var(--backdrop); }
  .flyer {
    position: absolute; left: 189px; top: 0;
    width: 822px; height: 1163px;
    background: var(--paper);
    font-family: "Open Sans", Arial, sans-serif;
    color: var(--body);
  }
  .title-band {
    position: absolute; left: 0; top: 37px; width: 322px; height: 78px;
    background: var(--red);
    clip-path: polygon(0 0, 100% 0, 95.6% 100%, 0 100%);
    color: #fff; font-family: "Arimo", Arial, sans-serif;
    padding: 14px 0 0 108px;
  }
  .title-band .band-name { font-size: 30px; font-weight: 700; line-height: 34px; letter-spacing: -0.3px; }
  .title-band .band-sub { font-size: 16.5px; font-weight: 700; line-height: 20px; }
  .brand-mark {
    position: absolute; left: 506px; top: 62px;
    font-family: "Open Sans", Arial, sans-serif; font-weight: 300;
    font-size: 47px; color: var(--red); letter-spacing: -0.5px; line-height: 56px;
  }
  .intro {
    position: absolute; left: 108px; top: 164px; width: 600px;
    font-family: "Arimo", Arial, sans-serif; font-weight: 700;
    font-size: 19.3px; line-height: 23.3px; color: var(--ink);
  }
  .principle { position: absolute; width: 290px; }
  .principle header { display: flex; align-items: center; height: 40px; gap: 12px; }
  .principle svg { flex: none; width: 44px; height: 40px; }
  .principle h3 {
    font-family: "Open Sans", Arial, sans-serif; font-weight: 600;
    font-size: 17.5px; color: var(--red); white-space: nowrap;
  }
  .principle p { font-size: 12.7px; line-height: 15px; margin-top: var(--gap, 10px); }
  .col-left { left: 108px; }
  .col-right { left: 454px; }
  .footer-name {
    position: absolute; left: 107px; top: 1085px;
    font-family: "Open Sans", Arial, sans-serif; font-weight: 300;
    font-size: 34px; color: var(--red-soft); line-height: 44px;
  }
  .footer-rule { position: absolute; left: 289px; top: 1107px; width: 456px; height: 1px; background: var(--red); }
  .contact {
    position: absolute; left: 290px; top: 1111px; display: flex; align-items: center; gap: 8px;
    font-family: "Arimo", Arial, sans-serif; font-size: 14px; color: var(--ink);
  }
  .contact svg { width: 13px; height: 13px; fill: var(--red); }
  .contact .item { display: flex; align-items: center; gap: 8px; margin-right: 4px; }
</style>
</head>
<body>
<main class="flyer">
  <div class="title-band">
    <div class="band-name">Brightwick</div>
    <div class="band-sub">Principles of Business</div>
  </div>
  <div class="brand-mark">Brightwick</div>

  <h1 class="intro">Brightwick Is Our Principles Of Business That Drive Our People, Systems And Processes To Give Assurance To Our Clients That Every Detail Matters.</h1>

  <!-- Left column -->
  <section class="principle col-left" style="top:264px; --gap:11px">
    <header>
      <svg viewBox="0 0 44 40" fill="var(--red)"><rect x="2" y="14" width="7" height="12"/><polygon points="9,14 30,5 30,35 9,26"/><rect x="32" y="3" width="4" height="34"/><rect x="11" y="26" width="6" height="10"/></svg>
      <h3>Client Experience</h3>
    </header>
    <p>Our promise is to pursue excellence and to continually deliver a solutions based service. We achieve this through active engagement, open channels of communication and a serviced led team with the dedicated resources to listen, engage and implement.</p>
  </section>

  <section class="principle col-left" style="top:412px; --gap:4px">
    <header>
      <svg viewBox="0 0 44 40" fill="none" stroke="var(--red)" stroke-width="3" stroke-linejoin="round"><path d="M3 14 L12 6 L20 12 L28 8 L40 18 L26 32 L14 22 Z"/><path d="M16 22 L22 28 M20 18 L27 25"/></svg>
      <h3>Loyalty</h3>
    </header>
    <p>We seek to develop a life-time relationship with our clients, building trust by acting with integrity, honesty and courtesy. We achieve this due to our expert approach to strata management and providing a responsive service to our clients.</p>
  </section>

  <section class="principle col-left" style="top:540px; --gap:10px">
    <header>
      <svg viewBox="0 0 44 40" fill="var(--red)"><polygon points="30,3 40,12 22,30 12,24"/><polygon points="12,24 22,30 4,38"/><circle cx="14" cy="30" r="2" fill="#fff"/></svg>
      <h3>Education and Guidance</h3>
    </header>
    <p>We endeavor to always be proactive in client education and guidance. This is achieved by our internal and external communications, comprehensive training programs and cross-departmental collaboration of knowledge sharing.</p>
  </section>

  <section class="principle col-left" style="top:690px; --gap:16px">
    <header style="gap:6px">
      <svg viewBox="0 0 44 40" fill="var(--red)"><polygon points="20,2 39,12 1,12"/><rect x="3" y="14" width="34" height="3"/><rect x="6" y="19" width="4" height="13"/><rect x="14" y="19" width="4" height="13"/><rect x="22" y="19" width="4" height="13"/><rect x="30" y="19" width="4" height="13"/><rect x="1" y="34" width="38" height="4"/></svg>
      <h3>Compliance &amp; Governance</h3>
    </header>
    <p>We engage and own a position of ‘every detail matters’. We give due diligence to the relevant state and national legislations with which we, our clients and our stakeholders must comply. We regulate and achieve this through a robust system of internal processes and protocols which structure and confirm our deliverables are in line with regulations.</p>
  </section>

  <section class="principle col-left" style="top:883px; --gap:10px">
    <header style="gap:18px">
      <svg viewBox="0 0 44 40" fill="var(--red)"><circle cx="16" cy="16" r="10"/><g stroke="var(--red)" stroke-width="5"><line x1="16" y1="2" x2="16" y2="30"/><line x1="2" y1="16" x2="30" y2="16"/><line x1="6" y1="6" x2="26" y2="26"/><line x1="26" y1="6" x2="6" y2="26"/></g><circle cx="16" cy="16" r="4" fill="#fff"/><circle cx="35" cy="30" r="6"/><g stroke="var(--red)" stroke-width="3"><line x1="35" y1="21" x2="35" y2="39"/><line x1="26" y1="30" x2="44" y2="30"/></g><circle cx="35" cy="30" r="2" fill="#fff"/></svg>
      <h3>Systems and processes</h3>
    </header>
    <p>We strive to be the best in our field, by implementing efficiencies without compromising service quality, accuracy or compliance. We continually seek to achieve this by reviewing, updating and adopting continuous improvement strategies, systems and quality processes that deliver outcomes.</p>
  </section>

  <!-- Right column -->
  <section class="principle col-right" style="top:265px; --gap:10px">
    <header style="gap:0">
      <svg viewBox="0 0 44 40" fill="none" stroke="var(--red)" stroke-width="3"><circle cx="18" cy="22" r="14"/><path d="M11 22 L17 28 L36 6" stroke-linecap="round"/></svg>
      <h3>Quality &amp; Commitment</h3>
    </header>
    <p>We invest in the recruitment and retention of a quality and diverse team of experienced professionals with a strong focus on continual professional development. As committed and skilled individuals, we actively promote the cross-departmental collaboration with one another to deliver a well rounded offering.</p>
  </section>

  <section class="principle col-right" style="top:433px; --gap:17px">
    <header style="gap:23px">
      <svg viewBox="0 0 44 40" fill="var(--red)"><path d="M2 2 L8 2 L14 32 L40 32" stroke="var(--red)" stroke-width="3" fill="none"/><rect x="16" y="8" width="14" height="12" transform="rotate(-12 23 14)"/><rect x="18" y="20" width="20" height="10"/><circle cx="16" cy="35" r="4"/></svg>
      <h3>Delivery</h3>
    </header>
    <p>We empower our teams to deliver an outstanding client service and to be accountable for their actions. We will make sure every detail matters, provide valuable insight and supply information in a clear and timely manner.</p>
  </section>

  <section class="principle col-right" style="top:578px; --gap:17px">
    <header style="gap:23px">
      <svg viewBox="0 0 44 40" fill="var(--red)"><polygon points="10,4 34,4 42,14 22,38 2,14"/><polyline points="2,14 42,14" stroke="#fff" stroke-width="2"/><polyline points="14,14 22,38 30,14" stroke="#fff" stroke-width="1.5" fill="none"/></svg>
      <h3>Integrity</h3>
    </header>
    <p>Our approach to strata management is bound by honesty and a strong set of moral principles. We act in our clients’ best interests with diligence and transparency for understanding and accountability.</p>
  </section>

  <section class="principle col-right" style="top:725px; --gap:15px">
    <header style="gap:16px">
      <svg viewBox="0 0 44 40" fill="var(--red)"><path d="M3 2 V37 H42" stroke="var(--red)" stroke-width="3" fill="none"/><rect x="8" y="24" width="6" height="11"/><rect x="17" y="18" width="6" height="17"/><rect x="26" y="22" width="6" height="13"/><rect x="35" y="12" width="6" height="23"/><polyline points="8,20 19,10 27,16 40,4" stroke="var(--red)" stroke-width="2.5" fill="none"/></svg>
      <h3>Continuous Improvement</h3>
    </header>
    <p>Our goal is to continually evolve to better our offering and to be adaptable and responsive to change. Our infrastructure supports us to continually mould into the business that is right for our clients.</p>
  </section>

  <section class="principle col-right" style="top:866px; --gap:11px">
    <header style="gap:13px">
      <svg viewBox="0 0 44 40" fill="none" stroke="var(--red)" stroke-width="2.5"><rect x="4" y="5" width="26" height="32"/><line x1="9" y1="13" x2="25" y2="13"/><line x1="9" y1="19" x2="25" y2="19"/><line x1="9" y1="25" x2="20" y2="25"/><line x1="9" y1="31" x2="18" y2="31"/><path d="M40 10 L26 32 L24 36 L28 33 L42 12 Z" fill="var(--red)"/></svg>
      <h3>Ethical Stance</h3>
    </header>
    <p>We aim to create a community of ethical business relationships where we contribute our values and services to give our clients outstanding reassurance of our abilities.</p>
  </section>

  <footer>
    <div class="footer-name">Brightwick</div>
    <div class="footer-rule"></div>
    <div class="contact">
      <span class="item"><svg viewBox="0 0 16 16"><path d="M3 1 L6 1 L7 5 L5 6.5 Q6.5 9.5 9.5 11 L11 9 L15 10 L15 13 Q14 15 12 15 Q2 13 1 3 Q1 1 3 1 Z"/></svg>1300 555 0192</span>
      <span class="item"><svg viewBox="0 0 16 16"><circle cx="8" cy="8" r="7"/><path d="M1 8 H15 M8 1 V15" stroke="#fff" stroke-width="1.2"/></svg>www.brightwick.com</span>
      <span class="item"><svg viewBox="0 0 16 16"><rect x="1" y="3" width="14" height="10"/><polyline points="1,3 8,9 15,3" stroke="#fff" stroke-width="1.3" fill="none"/></svg>info@brightwick.co</span>
    </div>
  </footer>
</main>
</body>
</html>
```